Single Page/Scrolling Design for Model Recruitment site

We need a design (and if you are capable, coding) for our company, Brimwell Parlour (LA as in Los Angeles). We like modern single page designs, hence the title for the project. We have already had a designer come up with a logo, which is attached. You're free to play around with the colors, although we want the site to have a feminine appeal to it.

The site is basically a recruitment project for girls who are interested in working as chat hosts for cam sites. We don't want anything cheesy that feels like a porn site. The inspiration for the logo (and the inspiration for the site) comes from the French and English salons of the late 18th century, where beautiful and intelligent women would gather to discuss a range of topics. We want the website to convey that this work is fun and exciting. Please keep these things in mind for the design.

As I mentioned, we like the modern look and feel of single page designs, especially because we don't have a ton of content. We just need an "About us" area, a "Work from Home" area, a "Work at The Brimwell Parlour" area, and "Contact Us" area which should have text boxes for entering email, subject, a message, etc.

The logo I mentioned is attached, as well as a very crude mockup of the layout of all the content I described.

Target Market(s)

Women age 18-35.

Industry/Entity Type

It Company

Font styles to use
Serif
Decorative
Script

Colors

Designer to choose colors to be used in the design.

Requirements
Should not have
• Images that are super sexual or even slightly pornographic. We want this to appeal to a broad range of women.

```html
<!DOCTYPE html>
<html lang="en">
<head>
<meta charset="utf-8">
<title>Brimwell Parlour — Contact</title>
<link href="https://fonts.googleapis.com/css2?family=Roboto+Condensed:wght@400;700&display=swap" rel="stylesheet">
<style>
  :root {
    --bg: #e6e4d6;
    --bg-light: #eeece2;
    --magenta: #b5387c;
    --magenta-deep: #a32d6c;
    --panel: #f4f2eb;
    --label: #8e1b2b;
    --button-top: #c2285c;
    --button-bottom: #8e1238;
    --white: #ffffff;
    --icon-ring: #e9e9e9;
    --icon-grey: #6b6b6b;
  }
  * { box-sizing: border-box; margin: 0; padding: 0; }
  html, body {
    width: 1200px;
    height: 684px;
    overflow: hidden;
  }
  body {
    position: relative;
    background: radial-gradient(ellipse at 65% 45%, var(--bg-light) 0%, var(--bg) 75%);
    font-family: "Roboto Condensed", "Arial Narrow", sans-serif;
  }

  .hero-portrait {
    position: absolute;
    left: 0;
    top: 0;
    width: 660px;
    height: 684px;
    background:
      radial-gradient(ellipse 38% 55% at 30% 50%, rgba(214, 184, 120, 0.85) 0%, rgba(214, 184, 120, 0) 100%),
      radial-gradient(ellipse 45% 40% at 35% 88%, rgba(238, 232, 216, 0.9) 0%, rgba(238, 232, 216, 0) 100%),
      radial-gradient(ellipse 12% 30% at 4% 78%, rgba(120, 82, 70, 0.55) 0%, rgba(120, 82, 70, 0) 100%),
      linear-gradient(90deg, rgba(200, 170, 120, 0.25) 0%, rgba(230, 228, 214, 0) 100%);
  }

  .site-nav {
    position: absolute;
    left: 145px;
    top: 0;
    width: 910px;
    height: 64px;
    background: var(--magenta);
    border-radius: 0 0 10px 10px;
  }
  .site-nav ul {
    list-style: none;
    display: flex;
    justify-content: center;
    align-items: center;
    gap: 32px;
    height: 64px;
    padding-bottom: 2px;
  }
  .site-nav li {
    color: var(--white);
    font-size: 19px;
    letter-spacing: -0.2px;
    white-space: nowrap;
  }
  .site-nav .contact { font-weight: 700; }

  .contact-tab {
    position: absolute;
    left: 460px;
    top: 114px;
    width: 240px;
    height: 134px;
  }
  .contact-tab .title {
    position: absolute;
    left: 0;
    width: 240px;
    top: 72px;
    text-align: center;
    color: var(--white);
    font-size: 30px;
    font-weight: 700;
    letter-spacing: -0.5px;
  }

  .contact-panel {
    position: absolute;
    left: 440px;
    top: 247px;
    width: 660px;
    height: 384px;
    background: var(--panel);
    box-shadow: 0 0 6px rgba(0, 0, 0, 0.12);
  }
  .field-label {
    position: absolute;
    left: 41px;
    color: var(--label);
    font-size: 19px;
    font-weight: 700;
    white-space: nowrap;
  }
  .field {
    position: absolute;
    left: 119px;
    width: 364px;
    height: 32px;
    background: var(--magenta);
    border: 1px solid var(--magenta-deep);
    border-radius: 2px;
    box-shadow: inset 0 1px 3px rgba(0, 0, 0, 0.25);
  }
  .field.message { height: 135px; }
  .submit-button {
    position: absolute;
    left: 525px;
    top: 318px;
    width: 102px;
    height: 31px;
    border-radius: 16px;
    background: linear-gradient(180deg, var(--button-top) 0%, var(--button-bottom) 100%);
    box-shadow: 0 1px 2px rgba(0, 0, 0, 0.35);
    color: var(--white);
    font-size: 14px;
    font-weight: 700;
    text-align: center;
    line-height: 31px;
    font-family: Arial, "Helvetica", sans-serif;
  }
</style>
</head>
<body>
  <div class="hero-portrait" role="img" aria-label="Photograph of a young woman with long blonde hair in a white dress, seated on an upholstered chair"></div>

  <nav class="site-nav">
    <ul>
      <li class="about">ABOUT US</li>
      <li class="train">TRAIN @ THE BRIMWELL PARLOUR</li>
      <li class="home">WORK FROM HOME</li>
      <li class="contact">CONTACT</li>
    </ul>
  </nav>

  <div class="contact-tab">
    <svg width="240" height="134" viewBox="0 0 240 134" aria-hidden="true">
      <polygon points="111,31 0,133 240,133" fill="var(--magenta)"/>
      <circle cx="111" cy="19" r="19" fill="var(--white)" stroke="var(--icon-ring)" stroke-width="2"/>
      <circle cx="111" cy="19" r="15" fill="#f2f2f2"/>
      <path d="M105.5 11.5c1-.6 2-.3 2.5.6l1.4 2.6c.4.8.2 1.6-.5 2.1l-1 .7c.6 1.9 2.2 3.9 4 4.9l.8-.9c.6-.6 1.4-.7 2.1-.3l2.5 1.6c.8.5 1 1.5.4 2.4-1 1.6-2.6 2.3-4.3 1.7-4.300-1.5-7.9-5.6-9.1-9.9-.5-1.9.1-3.6 1.2-4.5z" fill="var(--icon-grey)"/>
    </svg>
    <div class="title">Contact</div>
  </div>

  <section class="contact-panel" aria-label="Contact form">
    <span class="field-label" style="top:67px">Name</span>
    <div class="field" style="top:62px"></div>

    <span class="field-label" style="top:117px">Email</span>
    <div class="field" style="top:112px"></div>

    <span class="field-label" style="top:169px">Subject</span>
    <div class="field" style="top:164px"></div>

    <span class="field-label" style="top:219px">Message</span>
    <div class="field message" style="top:214px"></div>

    <div class="submit-button">Submit</div>
  </section>
</body>
</html>
```